NEW Escape Room. Fun, Dark and Mysterious.

Escape Room Website. Bookings and scheduling of appointments will be organised with Bolkit through the site. Most appointments will be created online through the booking system with some payments coming through in person by drop-ins. Groups will be from 2 - 8 people with a sliding scale of prices. We will start with one game playable and one saying coming soon. We will also eventually have 4 games up and running at once so will need it to be able to expand. We don't have any images of the rooms because it all relies heavily on mystery. Appointments are each 1 hour long with 30 minutes in between.

Target Market(s)

15-35 year olds

Coding

Coded - Design and coding required

Number of Pages Required

5+ page

Font styles to use
Decorative

Colors

Designer to choose colors to be used in the design.

Requirements
Must have
• Graphics showing what an escape room is.
• Page for About - What is an escape room
• Page for Games - Showing each of the different games which can be played with links to booking page. We have one game to start - the tailor's shadows. A victorian doctors office and serial killers. Then a game coming soon which is aztec/mayan/jungle/captain Worrel feel.
• FAQ Page
Nice to have
• Graphics for multiple players ie 2 players, 3 players, 4 players etc
• Dark and Mysterious feel.
• Inspiration from Cipher Vault, Lockwise Hall, Puzzle Harbor
Should not have
• Cartoony/childish. Pink.
• Not bloody or dripping letters etc - not cliche.
• Not horror themed.

```html
<!DOCTYPE html>
<html lang="en">
<head>
<meta charset="utf-8">
<title>Games – The Lantern Door</title>
<link rel="stylesheet" href="https://fonts.googleapis.com/css2?family=IM+Fell+English&family=IM+Fell+English+SC&family=Lato:wght@400;700&display=swap">
<style>
:root{
  --page:#121716;
  --card:#000000;
  --amber:#e8960c;
  --slot-off:#8a8a8a;
  --slot-off-text:#5a5a5a;
  --text:#ffffff;
  --muted:#b9b9b9;
  --footer:#0b0b0b;
}
*{margin:0;padding:0;box-sizing:border-box}
html,body{width:1200px;height:3564px;overflow:hidden}
body{background:var(--page);color:var(--text);font-family:"Lato",sans-serif;position:relative}
.abs{position:absolute}

.hero{left:0;top:0;width:1200px;height:496px;
  background:radial-gradient(ellipse 420px 300px at 830px 300px,#3b3632 0%,#1e1a18 45%,transparent 80%),linear-gradient(100deg,#070707 0%,#15110f 35%,#2a2320 60%,#0d0b0a 100%)}
.hero-fade{left:0;top:0;width:1200px;height:496px;background:linear-gradient(180deg,rgba(0,0,0,.55),transparent 25%,transparent 80%,rgba(0,0,0,.4))}
.brand{left:127px;top:55px;display:flex;align-items:center;gap:8px;font-family:"IM Fell English SC",serif;font-size:17px;color:var(--amber);line-height:1.1;width:110px}
.brand-dot{width:16px;height:16px;border-radius:50%;background:var(--amber);flex:none}
.nav{top:74px;font-size:15px;font-weight:700;color:#fff}
.nav.current{color:var(--amber)}
.nav-cta{left:913px;top:58px;width:161px;height:50px;border:2px solid var(--amber);border-radius:3px;color:var(--amber);font-weight:700;font-size:15px;display:flex;align-items:center;justify-content:center}
.page-title{left:125px;top:290px;font-family:"IM Fell English SC",serif;font-size:76px;letter-spacing:2px;line-height:1}

.game-card{left:125px;width:949px;background:var(--card);border-radius:14px;overflow:hidden}
.game-art{position:absolute;}
.game-name{position:absolute;left:66px;font-family:"IM Fell English SC",serif;font-size:40px;letter-spacing:.5px;line-height:1}
.game-tag{position:absolute;left:66px;font-family:"IM Fell English",serif;font-size:27px;color:var(--muted);line-height:1}
.difficulty{position:absolute;left:66px;font-family:"IM Fell English",serif;font-size:25px;display:flex;align-items:center;gap:14px;line-height:1}
.stars{color:var(--amber);font-size:26px;letter-spacing:3px}
.stars .off{color:#888}
.stars .half{background:linear-gradient(90deg,var(--amber) 50%,#888 50%);-webkit-background-clip:text;background-clip:text;color:transparent}
.facts{position:absolute;left:66px;font-family:"IM Fell English",serif;font-size:25px;display:flex;align-items:center;line-height:1}
.facts svg{margin-right:14px}
.facts .people{margin-left:42px}

.story{position:absolute;left:66px;top:426px;width:820px;font-family:"IM Fell English",serif;font-size:14.5px;line-height:23.5px}
.story p+p{margin-top:23.5px}
.hours{position:absolute;left:64px;top:763px;font-size:15px}
.date-picker{position:absolute;left:66px;top:808px;width:274px;height:45px;border:1.5px solid var(--amber);border-radius:3px;display:flex;align-items:center;padding:0 18px;font-size:15px;gap:16px}
.date-picker .caret{margin-left:auto}
.schedule{position:absolute;left:66px;top:905px;width:820px}
.day{height:95px}
.day-label{font-size:15px;height:33px}
.slots{display:flex;gap:7.6px}
.slot{width:84px;height:28px;border-radius:2px;background:var(--slot-off);color:var(--slot-off-text);font-family:"IM Fell English",serif;font-size:13px;display:flex;align-items:center;justify-content:center}
.slot.open{background:var(--amber);color:#fff;font-family:"Lato",sans-serif;font-weight:700}
.book-btn{position:absolute;left:398px;top:1621px;width:161px;height:50px;background:var(--amber);border-radius:2px;display:flex;align-items:center;justify-content:center;font-weight:700;font-size:16px}

.footer-band{left:0;top:3050px;width:1200px;height:514px;background:radial-gradient(ellipse at 50% 100%,#1f1f1f,transparent 70%),var(--footer)}
.footer-mark{left:555px;top:3010px;width:90px;height:90px;border-radius:50%;background:var(--amber)}
.footer-name{left:0;top:3170px;width:1200px;text-align:center;font-family:"IM Fell English SC",serif;font-size:30px;letter-spacing:1px}
.footer-link{top:3275px;font-size:15px;font-weight:700}
.social{top:3352px;width:29px;height:29px;background:#fff;border-radius:3px}
.copyright{left:0;top:3530px;width:1200px;text-align:center;font-size:10px;font-weight:700}
</style>
</head>
<body>

<header>
  <div class="abs hero" role="img" aria-label="Dark attic with a lone rocking chair under a sloped roof"></div>
  <div class="abs hero-fade"></div>
  <div class="abs brand"><span class="brand-dot"></span>The Lantern Door</div>
  <nav>
    <span class="abs nav" style="left:558px">About</span>
    <span class="abs nav current" style="left:641px">Games</span>
    <span class="abs nav" style="left:728px">Contact Us</span>
    <span class="abs nav" style="left:843px">FAQ</span>
    <span class="abs nav-cta">BOOK A GAME</span>
  </nav>
  <h1 class="abs page-title">GAMES</h1>
</header>

<main>
  <section class="abs game-card" style="top:595px;height:1750px">
    <div class="game-art" role="img" aria-label="Masked surgeon figure in a dim Victorian operating room" style="left:401px;top:0;width:505px;height:388px;background:radial-gradient(ellipse 230px 190px at 330px 220px,#5e5560 0%,#2a2630 45%,#000 85%)"></div>
    <h2 class="game-name" style="top:66px">THE TAILOR'S SHADOWS</h2>
    <p class="game-tag" style="top:116px">The Doctor Will See You Now</p>
    <div class="difficulty" style="top:216px">Difficulty <span class="stars">★★★★<span class="off">★</span></span></div>
    <div class="facts" style="top:263px">
      <svg width="22" height="22" viewBox="0 0 22 22"><circle cx="11" cy="11" r="9.5" fill="none" stroke="#fff" stroke-width="1.5"/><path d="M11 5v6H7" fill="none" stroke="#fff" stroke-width="1.5"/></svg>60 min
      <span class="people"><svg width="22" height="22" viewBox="0 0 22 22"><circle cx="11" cy="6" r="5" fill="#fff"/><path d="M1 22c0-6 4.5-9 10-9s10 3 10 9z" fill="#fff"/></svg></span>2–8 people
    </div>
    <div class="story">
      <p>Paris in the winter of 1822. The nights are long and unseasonably cold. The streets are dark and uncharacteristically quiet. But for the latter there is a truth shrouded in fear that keeps the populous from venturing after dark. Every week icy sheets of blood gleen the streets of Paris at dawn. People are disappearing. It began a few years ago, first taking ladies of the night or drunkards slovenly staggering back to their hovels. But recently the murders have escalated, the killers tastes have evolved and so has the knife that bleeds the victims.</p>
      <p>And yet, with the hundreds missing there has never been a body. At most on a crisp winters morning season last, a solitary finger lay in the glistening puddle of blood, seemingly frozen and cracked away when the body was removed.</p>
      <p>But alas, a glimmer of hope in a package that should otherwise spell more impending doom for a town not accustomed to the horrors of Paris in this day. A body was found. Detectives raced to investigate but custody was soon given to the doctor to perform the autopsy and find cause of death.</p>
    </div>
    <p class="hours">Business is open by appointment. Hours start from 8am to the end of last game at 9pm.</p>
    <div class="date-picker">
      <svg width="17" height="16" viewBox="0 0 17 16"><rect x="0" y="2" width="17" height="14" fill="#fff"/><rect x="0" y="2" width="17" height="4" fill="#ccc"/><rect x="3" y="0" width="2" height="4" fill="#fff"/><rect x="12" y="0" width="2" height="4" fill="#fff"/></svg>
      13 February, 2020
      <svg class="caret" width="17" height="12" viewBox="0 0 17 12"><path d="M0 0h17L8.5 12z" fill="var(--amber)"/></svg>
    </div>
    <div class="schedule">
      <div class="day"><p class="day-label">Thursday, 13 February</p><div class="slots"><span class="slot">8:00 am</span><span class="slot">9:30 am</span><span class="slot open">11:00 am</span><span class="slot">12:30 pm</span><span class="slot">14:00 pm</span><span class="slot">15:30 pm</span><span class="slot">17:00 pm</span><span class="slot">18:30 pm</span><span class="slot open">20:00 pm</span></div></div>
      <div class="day"><p class="day-label">Friday, 14 February</p><div class="slots"><span class="slot open">8:00 am</span><span class="slot">9:30 am</span><span class="slot">11:00 am</span><span class="slot open">12:30 pm</span><span class="slot">14:00 pm</span><span class="slot open">15:30 pm</span><span class="slot">17:00 pm</span><span class="slot">18:30 pm</span><span class="slot">20:00 pm</span></div></div>
      <div class="day"><p class="day-label">Saturday, 15 February</p><div class="slots"><span class="slot">8:00 am</span><span class="slot">9:30 am</span><span class="slot">11:00 am</span><span class="slot">12:30 pm</span><span class="slot open">14:00 pm</span><span class="slot">15:30 pm</span><span class="slot">17:00 pm</span><span class="slot">18:30 pm</span><span class="slot">20:00 pm</span></div></div>
      <div class="day"><p class="day-label">Sunday, 16 February</p><div class="slots"><span class="slot">8:00 am</span><span class="slot">9:30 am</span><span class="slot">11:00 am</span><span class="slot">12:30 pm</span><span class="slot">14:00 pm</span><span class="slot open">15:30 pm</span><span class="slot">17:00 pm</span><span class="slot">18:30 pm</span><span class="slot open">20:00 pm</span></div></div>
      <div class="day"><p class="day-label">Monday, 17 February</p><div class="slots"><span class="slot open">8:00 am</span><span class="slot open">9:30 am</span><span class="slot">11:00 am</span><span class="slot">12:30 pm</span><span class="slot open">14:00 pm</span><span class="slot">15:30 pm</span><span class="slot open">17:00 pm</span><span class="slot">18:30 pm</span><span class="slot open">20:00 pm</span></div></div>
      <div class="day"><p class="day-label">Tuesday, 18 February</p><div class="slots"><span class="slot open">8:00 am</span><span class="slot">9:30 am</span><span class="slot">11:00 am</span><span class="slot open">12:30 pm</span><span class="slot open">14:00 pm</span><span class="slot">15:30 pm</span><span class="slot open">17:00 pm</span><span class="slot open">18:30 pm</span><span class="slot open">20:00 pm</span></div></div>
      <div class="day"><p class="day-label">Wednesday, 19 February</p><div class="slots"><span class="slot open">8:00 am</span><span class="slot open">9:30 am</span><span class="slot">11:00 am</span><span class="slot open">12:30 pm</span><span class="slot open">14:00 pm</span><span class="slot open">15:30 pm</span><span class="slot">17:00 pm</span><span class="slot">18:30 pm</span><span class="slot open">20:00 pm</span></div></div>
    </div>
    <span class="book-btn">BOOK NOW</span>
  </section>

  <section class="abs game-card" style="top:2418px;height:408px">
    <div class="game-art" role="img" aria-label="Carved stone mask relief from an ancient jungle temple" style="left:456px;top:25px;width:450px;height:339px;background:radial-gradient(ellipse 230px 180px at 240px 160px,#7a5a45 0%,#4a3a30 45%,#000 92%)"></div>
    <h2 class="game-name" style="top:64px">XOLOTEC'S TOMB</h2>
    <p class="game-tag" style="top:114px">Coming Soon</p>
    <div class="difficulty" style="top:214px">Difficulty <span class="stars">★★★<span class="half">★</span><span class="off">★</span></span></div>
    <div class="facts" style="top:261px">
      <svg width="22" height="22" viewBox="0 0 22 22"><circle cx="11" cy="11" r="9.5" fill="none" stroke="#fff" stroke-width="1.5"/><path d="M11 5v6H7" fill="none" stroke="#fff" stroke-width="1.5"/></svg>60 min
      <span class="people"><svg width="22" height="22" viewBox="0 0 22 22"><circle cx="11" cy="6" r="5" fill="#fff"/><path d="M1 22c0-6 4.5-9 10-9s10 3 10 9z" fill="#fff"/></svg></span>2–8 people
    </div>
  </section>
</main>

<footer>
  <div class="abs footer-band"></div>
  <div class="abs footer-mark"></div>
  <p class="abs footer-name">THE LANTERN DOOR</p>
  <span class="abs footer-link" style="left:443px">About</span>
  <span class="abs footer-link" style="left:525px">Games</span>
  <span class="abs footer-link" style="left:612px">Contact Us</span>
  <span class="abs footer-link" style="left:727px">FAQ</span>
  <span class="abs social" style="left:517px" aria-label="Social link"></span>
  <span class="abs social" style="left:585px" aria-label="Social link"></span>
  <span class="abs social" style="left:652px" aria-label="Social link"></span>
  <p class="abs copyright">©2020 The Lantern Door. All Rights Reserved.</p>
</footer>

</body>
</html>
```